Skin care manufacturer looking for packaging design for new skin care brand.

We need a design and logo for a skin care brand to be sold at retail stores and online in the United States and Europe. The design will be for 1.7oz - 2oz serums that will not have a retail box. The name of the brand is Orvia Lune and should be a luxurious brand that is approachable. The brand will consist of 4 face serums - Vitamin C, Collagen, Retinol and Hyaluronic Acid that all contain Dead Sea Minerals. Images shown are for inspiration only. Color of bottles can be varied based on design and bottles can be screen printed or labeled.

```html
<!DOCTYPE html>
<html lang="en">
<head>
<meta charset="utf-8">
<title>Orvia Lune – 4 Facial Serums Label Range</title>
<link rel="stylesheet" href="https://fonts.googleapis.com/css2?family=Italiana&family=Poiret+One&family=Montserrat:wght@400;500;600&display=swap">
<style>
  :root {
    --canvas: #e9e9ea;
    --noir-top: #2a2a2a;
    --noir-bottom: #0b0b0b;
    --gold: #d9b57c;
    --violet-top: #8b3ff2;
    --violet-bottom: #d547d6;
    --violet-edge: #5a1aa8;
    --ocean-top: #3a8fd6;
    --ocean-bottom: #1c62b5;
    --ocean-edge: #0f3f7a;
    --white: #ffffff;
  }
  * { margin: 0; padding: 0; box-sizing: border-box; }
  html, body { width: 1200px; height: 1079px; overflow: hidden; }
  body {
    background: var(--canvas);
    position: relative;
    font-family: "Montserrat", sans-serif;
  }
  .label {
    position: absolute;
    top: 285px;
    width: 302px;
    height: 508px;
    border-radius: 26px;
    overflow: hidden;
  }
  .label > * { position: absolute; }
  .display { font-family: "Italiana", serif; font-weight: 400; }
  .numeral { font-family: "Poiret One", sans-serif; font-weight: 400; line-height: 1; }

  /* Noir edition */
  .label--noir {
    left: 98px;
    background: linear-gradient(90deg, var(--noir-bottom) 0%, var(--noir-top) 30%, #333 55%, var(--noir-bottom) 100%);
    color: var(--gold);
    text-align: center;
  }
  .label--noir .brand { left: 0; right: 0; top: 64px; font-size: 34px; letter-spacing: 1px; }
  .label--noir .count { left: 0; right: 0; top: 122px; font-size: 160px; }
  .label--noir .title { left: 0; right: 0; top: 262px; font-size: 29px; letter-spacing: 0.5px; }
  .label--noir .actives { left: 0; right: 0; top: 364px; font-size: 13px; font-weight: 500; letter-spacing: 0.8px; line-height: 16px; }
  .label--noir .volume { left: 0; right: 0; top: 456px; font-size: 10px; }

  /* Violet edition */
  .label--violet {
    left: 449px;
    background:
      linear-gradient(90deg, rgba(70,10,140,0.45) 0%, rgba(255,255,255,0) 18%, rgba(255,255,255,0) 85%, rgba(70,10,140,0.5) 100%),
      linear-gradient(180deg, var(--violet-top) 0%, #b040e0 50%, var(--violet-bottom) 85%, var(--violet-edge) 100%);
    color: var(--white);
  }
  .label--violet .brand-vertical {
    left: 20px; top: 462px;
    transform: rotate(-90deg);
    transform-origin: 0 0;
    font-size: 84px; line-height: 1; white-space: nowrap; letter-spacing: -2px;
  }
  .label--violet .count { left: 144px; top: 116px; font-size: 106px; }
  .label--violet .title { left: 146px; top: 214px; font-size: 32px; line-height: 0.9; }
  .label--violet .actives { left: 146px; top: 380px; font-size: 10px; font-weight: 600; line-height: 13px; }
  .label--violet .volume { left: 148px; top: 451px; font-size: 10px; }

  /* Ocean edition */
  .label--ocean {
    left: 770px;
    background:
      linear-gradient(90deg, rgba(10,40,90,0.55) 0%, rgba(255,255,255,0) 15%, rgba(255,255,255,0) 85%, rgba(10,40,90,0.55) 100%),
      linear-gradient(180deg, var(--ocean-top) 0%, var(--ocean-bottom) 80%, var(--ocean-edge) 100%);
    color: var(--white);
  }
  .label--ocean .brand { left: 0; right: 0; text-align: center; top: 42px; font-size: 44px; white-space: nowrap; }
  .label--ocean .count { left: 44px; top: 178px; font-size: 132px; }
  .label--ocean .title { left: 113px; top: 240px; font-size: 34px; line-height: 1; }
  .label--ocean .rule { left: 50px; top: 343px; width: 5px; height: 55px; border-radius: 3px; background: var(--white); }
  .label--ocean .actives { left: 66px; top: 340px; font-size: 14px; line-height: 18px; }
  .label--ocean .volume { left: 49px; top: 462px; font-size: 14px; }
</style>
</head>
<body>

<section class="label label--noir" aria-label="Orvia Lune noir serum label">
  <div class="brand display">ORVIA LUNE</div>
  <div class="count numeral">4</div>
  <div class="title display">FACIAL SERUMS</div>
  <div class="actives">• VITAMIN C &nbsp;• COLLAGEN<br>• RETINOL &amp;<br>• HYALURONIC ACID</div>
  <div class="volume">1.7 FL. oz. (50ml)</div>
</section>

<section class="label label--violet" aria-label="Orvia Lune violet serum label">
  <div class="brand-vertical display">ORVIA LUNE</div>
  <div class="count numeral">4</div>
  <div class="title display">FACIAL<br>SERUMS</div>
  <div class="actives">• Vitamin C &nbsp;• Collagen<br>• Retinol &amp;<br>• Hyaluronic Acid</div>
  <div class="volume">1.7 FL. oz. (50ml)</div>
</section>

<section class="label label--ocean" aria-label="Orvia Lune ocean serum label">
  <div class="brand display">Orvia Lune</div>
  <div class="count numeral">4</div>
  <div class="title display">Facial<br>Serums</div>
  <div class="rule"></div>
  <div class="actives">▪ Vitamin C<br>▪ Collagen<br>▪ Retinol &amp; Hyaluronic Acid</div>
  <div class="volume">1.7 FL. oz. (50ml)</div>
</section>

</body>
</html>
```